2 banner Designs

I have a trade show in Vegas and I want you to design 2 banners that are Graphic size: 33.5" (W) x 80.5" (H). The banners are standing in the booth.

I am looking for a luxury modern feel for the banners. The banners are going to be important to attract customers in.

I am showing latex foam pillows and latex mattress. The company is called Verdant Rest. Please use any photos from our website.

https://www.lumivaslee.net/verdantrest

Banner 1

Introducing our Verdant Rest mattress, a perfect harmony of luxurious organic cushioning and an advanced internal, zoned pressure-point support system.

Experience unparalleled back support and remarkable durability, all in one exceptional sleep solution.

Verdant Rest Mattress

HVRA-certified organic cotton
HVRA-certified organic wool
2 “ HVLA-certified organic latex
8” Pocket Coils
1’’ HVLA-certified organic latex

Banner 2

Verdant Rest Pillows

We developed a customizable pillow with the perfect amount of comfort and support.

Our New Latex pillow has an adjustable fill with 90% Natural Latex and 10% Traceable Wool.  Our pillow cover is made from HVRA-certified organic cotton.

FILE REQUIREMENTS
We can take the file in the following file formats:

Single Page PDF (Preferred)
JPG (Preferred)
PSD – Please flatten file
EPS – Please embed all images. Outline all fonts and strokes.
Ai – Please embed all images. Outline all fonts and strokes.
Don't Include Crop Marks or Bleed

Artwork at either full scale, 1/2 scale or 1/10 scale that is fine. Just make sure that when the file is being set up the DPI is compensated according to the scale.

Full Scale – 150 DPI
1/2 Scale – 300 DPI
1/10 Scale – 450 DPI
***Remove EVERYTHING from your file that you do not want printed on the final product - especially hidden layers and template guidelines.

- Flatten all Objects/Gradients/Swatches/Symbols/Special Effects/Transparencies
- Outline all text
- Flattened PDF (Single Page) or JPEG file types only
- Remove all crop marks/bleed otherwise they will be printed
- File must be the same exact size as what is ordered (exception is Gallery wrap Fold Edge and Products with templates)
- CMYK only (we do not print Pantone/5th/Spot/RGB)
- 150 dpi
- If using a template, the file uploaded to our site should match the exact "template size" (different than "graphic size").
- Do not scale template files, just flatten them and save at 150 dpi
- Files over 200" can be scaled
- Under 300 mb for upload

- Make sure all objects are embedded and flattened (we do not print Non-Native Art).
- If the file is made in Indesign, please flatten the file in Illustrator or Photoshop and export to a JPEG ONLY as we don't recommend using Indesign at our facility.

- If using Compound Paths to create transparencies/shapes, please completely rasterize or flatten them into the file or they may print incorrectly.

- We do not have specific measurements for Panel jobs. If you are printing in Panels, please make sure you are providing a minimum of 1" overlay in your files.

Please make sure that your file is in CMYK format for print production with no bleed. It is not required.

```html
<!DOCTYPE html>
<html lang="en">
<head>
<meta charset="utf-8">
<title>Verdant Rest – Trade Show Banners</title>
<link rel="stylesheet" href="https://fonts.googleapis.com/css2?family=Marcellus&family=Arimo:wght@400;700&display=swap">
<style>
  :root {
    --stage: #8a918d;
    --brand-green: #688b2a;
    --pale-green: #b9cf9e;
    --paper: #ffffff;
    --ink: #2b2b2b;
    --display: "Marcellus", serif;
    --body: "Arimo", Arial, sans-serif;
  }
  * { margin: 0; padding: 0; box-sizing: border-box; }
  html, body { width: 1134px; height: 1200px; overflow: hidden; background: var(--stage); }
  .banner {
    position: absolute; top: 63px; width: 447px; height: 1073px;
    background: linear-gradient(to bottom, var(--paper) 0, var(--paper) 324px, var(--pale-green) 640px);
    overflow: hidden; box-shadow: 0 6px 8px rgba(0,0,0,.25);
  }
  .banner--mattress { left: 85px; }
  .banner--pillows { left: 603px; }
  .banner__art { position: absolute; inset: 0; }
  .layer { position: absolute; left: 0; width: 100%; text-align: center; }
  .brand-name {
    top: 100px; font-family: var(--display); font-size: 30px; color: var(--brand-green);
    letter-spacing: 1px;
  }
  .headline {
    top: 160px; font-family: var(--display); font-size: 33px; line-height: 34px;
    color: var(--brand-green); font-weight: 400;
  }
  .intro { font-family: var(--body); font-size: 17px; line-height: 21px; color: var(--ink); }
  .banner--mattress .intro { top: 269px; }
  .banner--pillows .intro { top: 266px; }
  .lead { top: 362px; font-family: var(--body); font-weight: 700; font-size: 12.5px; line-height: 16px; color: var(--ink); }
  .spec-box {
    position: absolute; border: 2px solid var(--brand-green); border-radius: 6px;
  }
  .banner--mattress .spec-box { left: 92px; top: 409px; width: 263px; height: 129px; }
  .banner--pillows .spec-box { left: 49px; top: 339px; width: 347px; height: 147px; }
  .spec-box__tag {
    position: absolute; background: var(--brand-green); color: var(--paper);
    font-family: var(--body); font-weight: 700; font-size: 13px; border-radius: 12px;
    display: flex; align-items: center; justify-content: center;
  }
  .banner--mattress .spec-box__tag { left: 104px; top: 401px; width: 238px; height: 23px; }
  .banner--pillows .spec-box__tag { left: 63px; top: 330px; width: 320px; height: 24px; }
  .spec-list { list-style: none; top: 491px; }
  .spec-list li { font-family: var(--body); font-weight: 700; font-size: 12.5px; line-height: 20px; color: var(--ink); }
  .banner--mattress .spec-list { top: 491px; }
  .fill-stat { font-family: var(--display); color: var(--brand-green); }
  .fill-stat__value { font-size: 30px; line-height: 30px; }
  .fill-stat__value small { font-size: 19px; }
  .fill-stat__label { font-family: var(--display); font-size: 13px; color: var(--ink); line-height: 15px; }
  .fill-stat--latex { top: 354px; }
  .fill-stat--wool { top: 426px; }
  .fill-and {
    position: absolute; left: 204px; top: 412px; width: 37px; height: 14px; border-radius: 7px;
    background: var(--brand-green); color: var(--paper); font-family: var(--display); font-size: 12px;
    line-height: 14px; text-align: center;
  }
  .cover-note { top: 497px; font-family: var(--body); font-weight: 700; font-size: 12.5px; color: var(--ink); }
  .cover-note strong { display: block; font-size: 19.5px; color: var(--brand-green); margin-top: 4px; }
</style>
</head>
<body>

<section class="banner banner--mattress">
  <svg class="banner__art" viewBox="0 0 447 1073" width="447" height="1073">
    <defs>
      <linearGradient id="bedroom-tones" x1="0" y1="0" x2="0" y2="1">
        <stop offset="0" stop-color="#ecebe8"/>
        <stop offset="0.45" stop-color="#d9d6cf"/>
        <stop offset="0.7" stop-color="#9fb0ad"/>
        <stop offset="1" stop-color="#8a6f52"/>
      </linearGradient>
    </defs>
    <path d="M148 0 C260 10 330 60 447 141 L447 0 Z" fill="var(--brand-green)"/>
    <path d="M0 547 C150 530 260 560 447 625 L447 1073 L0 1073 Z" fill="var(--brand-green)"/>
    <path d="M0 560 C160 545 270 600 447 690" stroke="var(--paper)" stroke-width="4" fill="none"/>
    <path d="M0 571 C130 555 240 610 447 725 L447 952 C300 1010 150 1040 0 1049 Z" fill="url(#bedroom-tones)" role="img" aria-label="Photo of a bedroom with a made bed, wooden headboard and bedside lamps"/>
    <path d="M0 1060 C200 1050 330 1005 447 978" stroke="var(--paper)" stroke-width="4" fill="none"/>
  </svg>
  <p class="layer brand-name">VERDANT REST</p>
  <h1 class="layer headline">INTRODUCING OUR<br>VERDANT REST<br>MATTRESS</h1>
  <p class="layer intro">a perfect harmony of luxurious organic<br>cushioning and an advanced internal,<br>zoned pressure-point support system.</p>
  <p class="layer lead">Experience unparalleled back support and remarkable durability,<br>all in one exceptional sleep solution.</p>
  <div class="spec-box"></div>
  <div class="spec-box__tag">VERDANT REST MATTRESS</div>
  <ul class="layer spec-list" style="top:490px; transform:translateY(-64px)">
    <li>HVRA-certified organic cotton</li>
    <li>HVRA-certified organic wool</li>
    <li>2 “ HVLA-certified organic latex</li>
    <li>8” Pocket Coils</li>
    <li>1’’ HVLA-certified organic latex</li>
  </ul>
</section>

<section class="banner banner--pillows">
  <svg class="banner__art" viewBox="0 0 447 1073" width="447" height="1073">
    <defs>
      <linearGradient id="pillow-tones" x1="0" y1="0" x2="1" y2="1">
        <stop offset="0" stop-color="#f1ede6"/>
        <stop offset="0.5" stop-color="#e6dccd"/>
        <stop offset="0.8" stop-color="#b9865a"/>
        <stop offset="1" stop-color="#f4f2ee"/>
      </linearGradient>
    </defs>
    <path d="M148 0 C260 10 330 60 447 141 L447 0 Z" fill="var(--brand-green)"/>
    <path d="M0 547 C150 530 260 560 447 625 L447 1073 L0 1073 Z" fill="var(--brand-green)"/>
    <path d="M0 560 C160 545 270 600 447 690" stroke="var(--paper)" stroke-width="4" fill="none"/>
    <path d="M0 571 C130 555 240 610 447 725 L447 952 C300 1010 150 1040 0 1049 Z" fill="url(#pillow-tones)" role="img" aria-label="Photo of a smiling woman on a bed hugging a latex pillow"/>
    <path d="M0 1060 C200 1050 330 1005 447 978" stroke="var(--paper)" stroke-width="4" fill="none"/>
  </svg>
  <p class="layer brand-name">VERDANT REST</p>
  <h1 class="layer headline">INTRODUCING OUR<br>VERDANT REST<br>PILLOWS</h1>
  <p class="layer intro">We developed a customizable pillow with<br>the perfect amount of comfort and support.</p>
  <div class="spec-box"></div>
  <div class="spec-box__tag">Our New Latex pillow has an adjustable fill with</div>
  <div class="layer fill-stat fill-stat--latex">
    <p class="fill-stat__value">90<small>%</small></p>
    <p class="fill-stat__label">NATURAL LATEX</p>
  </div>
  <span class="fill-and">and</span>
  <div class="layer fill-stat fill-stat--wool">
    <p class="fill-stat__value">10<small>%</small></p>
    <p class="fill-stat__label">TRACEABLE WOOL.</p>
  </div>
  <p class="layer cover-note">Our pillow cover is made from<strong>HVRA-certified organic cotton.</strong></p>
</section>

</body>
</html>
```